Flyer Design - Child Care Centre

I need a flyer design (d/sided), full colour for a Child Care Centre that I have recently bought. Check out my website (tiny-sprouts.com.au) for information on what we do, our services, philosophy, fees and hours of operation.

The purpose of this flyer is to advertise our services as a child care centre (under new management) to the local community and with various hospitals.

The flyer should embody our philosophy, the text on my home page (particularly our QX focus) and some of the parent testimonials. It should also include my logo and Zibb (refer attached AI and jpeg files, eps available on request).

Feel free to add stock photo's of kids and cartoon characters and use the following CMYK colours if incorporating any coloured text. Green: C-78, M-0, Y-100, K-0 Magenta: C-0, M-100, Y-33, K-10

```html
<!DOCTYPE html>
<html lang="en">
<head>
<meta charset="utf-8">
<title>Tiny Sprouts – Flyer</title>
<link href="https://fonts.googleapis.com/css2?family=Fredoka:wght@500;600&family=Open+Sans:wght@400;600;700&family=Courgette&display=swap" rel="stylesheet">
<style>
  :root {
    --green: #22b61f;
    --magenta: #a8178f;
    --purple: #9b1c8f;
    --ink: #222222;
    --paper: #ffffff;
    --backdrop: #eceff1;
  }
  * { margin: 0; padding: 0; box-sizing: border-box; }
  html, body { width: 1200px; height: 900px; overflow: hidden; }
  body { background: var(--backdrop); font-family: "Open Sans", sans-serif; color: var(--ink); position: relative; }

  .flyer { position: absolute; background: var(--paper); overflow: hidden; box-shadow: 0 6px 18px rgba(0,0,0,.25); }
  .flyer svg.shapes { position: absolute; inset: 0; }
  .flyer-front { left: 70px; top: 40px; width: 620px; height: 460px; z-index: 2; }
  .flyer-back { left: 475px; top: 385px; width: 680px; height: 480px; z-index: 1; }

  .photo { position: absolute; }
  .front-photo { left: 0; top: 0; width: 255px; height: 392px;
    background: radial-gradient(ellipse at 45% 40%, #f6d9c8 0%, #f2b6cf 35%, #f7f2f4 75%, #ffffff 100%); }
  .back-photo { left: 398px; top: 176px; width: 250px; height: 182px;
    background: linear-gradient(120deg, #f3e4dc 0%, #d9a9b7 35%, #8a3d8f 70%, #5f2a6a 100%); }

  .brand { position: absolute; text-align: center; }
  .brand-name { display: flex; align-items: center; justify-content: center; gap: 8px;
    font-family: "Fredoka", sans-serif; font-weight: 600; color: var(--green); line-height: 1; }
  .brand-dot { border-radius: 50%; background: var(--magenta); flex: none; }
  .brand-tag { font-family: "Fredoka", sans-serif; font-weight: 500; color: var(--green); margin-top: 6px; }
  .front-brand { left: 330px; top: 136px; width: 280px; }
  .front-brand .brand-name { font-size: 38px; }
  .front-brand .brand-dot { width: 20px; height: 20px; }
  .front-brand .brand-tag { font-size: 14px; }
  .back-brand { left: 425px; top: 122px; width: 240px; }
  .back-brand .brand-name { font-size: 30px; }
  .back-brand .brand-dot { width: 16px; height: 16px; }
  .back-brand .brand-tag { font-size: 11px; }

  .tagline { position: absolute; left: 262px; top: 212px; font-family: "Courgette", cursive;
    color: var(--magenta); font-size: 19px; line-height: 1.15; }
  .intro { position: absolute; left: 262px; top: 268px; width: 180px; font-size: 9.6px; line-height: 1.5; }

  .welcome { position: absolute; left: 462px; top: 212px; width: 142px; height: 142px; border-radius: 50%;
    background: var(--magenta); border: 4px solid var(--paper); outline: 3px solid var(--magenta);
    display: flex; flex-direction: column; align-items: center; justify-content: center; text-align: center;
    color: var(--paper); font-size: 12px; line-height: 1.2; }
  .welcome strong { font-size: 17px; font-weight: 700; }

  .phone { position: absolute; font-family: "Fredoka", sans-serif; font-weight: 600; color: var(--paper); white-space: nowrap; }
  .front-phone { right: 18px; top: 364px; font-size: 22px; }
  .back-phone { left: 362px; top: 366px; font-size: 32px; }

  .web { position: absolute; font-family: "Fredoka", sans-serif; font-weight: 500; color: var(--paper); letter-spacing: .5px; white-space: nowrap; }
  .front-web { left: 48px; top: 416px; font-size: 20px; }
  .back-web { left: 364px; top: 410px; font-size: 18px; }

  .philosophy { position: absolute; left: 50px; top: 62px; width: 340px; }
  .philosophy h2 { font-family: "Fredoka", sans-serif; font-weight: 600; font-size: 24px; color: var(--magenta); margin-bottom: 2px; }
  .philosophy p { font-size: 9.6px; font-weight: 700; line-height: 1.2; margin-bottom: 5px; }

  .contact { position: absolute; left: 50px; top: 342px; color: var(--paper); font-size: 11px; line-height: 1.35; }
  .contact .hours { font-weight: 700; }

  .social { position: absolute; left: 50px; top: 448px; display: flex; gap: 22px; font-size: 10px; }
  .social span { display: flex; align-items: center; gap: 6px; }
  .social i { width: 16px; height: 16px; background: var(--purple); display: inline-block; }
</style>
</head>
<body>

  <section class="flyer flyer-front">
    <svg class="shapes" width="620" height="460" viewBox="0 0 620 460">
      <polygon points="250,0 620,0 620,18" fill="var(--green)"/>
      <polygon points="300,400 620,330 620,400" fill="var(--purple)"/>
      <polygon points="0,392 620,398 620,460 0,460" fill="var(--green)"/>
    </svg>
    <div class="photo front-photo" role="img" aria-label="Photo of a toddler playing with a toy duck and stacking rings"></div>
    <div class="brand front-brand">
      <div class="brand-name"><span class="brand-dot"></span>Tiny Sprouts</div>
      <div class="brand-tag">Early Development &amp; Education Centre</div>
    </div>
    <div class="tagline">Unleash your<br>Childs imagination!</div>
    <p class="intro">We provide a child care environment that enhances the emotional and physical health of your child, stimulates the children's involvement in activities and encourages self-esteem and a sense of achievement.</p>
    <div class="welcome"><strong>WELCOME</strong>to Tiny Sprouts<br>Early Development<br>&amp;<br>Education Centre</div>
    <div class="phone front-phone">Ph.(08) 9000 4127</div>
    <div class="web front-web">www.tiny-sprouts.com.au</div>
  </section>

  <section class="flyer flyer-back">
    <svg class="shapes" width="680" height="480" viewBox="0 0 680 480">
      <polygon points="0,0 680,0 680,28 0,18" fill="var(--green)"/>
      <rect x="0" y="334" width="680" height="106" fill="var(--magenta)"/>
    </svg>
    <div class="philosophy">
      <h2>Our Philosophy</h2>
      <p>Every child is unique and we believe that success and growth comes from learning with encouragement and praise.</p>
      <p>Our educator's focus is on building every child's self esteem and confidence through positive feedback, we nurture their natural strengths.</p>
      <p>A child sees the world around them with wonder and awe we believe in encouraging their natural curiosity.</p>
      <p>The QX Convention on the Rights of the Child states that 'All children have the right to an education that lays a foundation for the rest of their lives, maximises their ability and respects their family, languages, cultural and other identities.</p>
      <p>Our educators, guided by the Early Years Learning Framework will reinforce in their daily practice the principles as laid out in the QX Convention on the Rights of the Child.</p>
      <p>Tiny Sprouts offers Long Day Care, Before &amp; After School Care (OSHC) and Vacation Care for children aged 6 weeks to 12 years.</p>
    </div>
    <div class="brand back-brand">
      <div class="brand-name"><span class="brand-dot"></span>Tiny Sprouts</div>
      <div class="brand-tag">Early Development &amp; Education Centre</div>
    </div>
    <div class="photo back-photo" role="img" aria-label="Photo of an educator reading a picture book with a young girl"></div>
    <div class="contact">
      58 Banksia Road,<br>
      Wattle Grove, WA 6107<br>
      Email: enquiries@tiny-sprouts.com.au<br>
      <span class="hours">Open Monday - Friday 6:00am - 6:00pm</span><br>
      (except public holidays)
    </div>
    <div class="phone back-phone">Ph.(08) 9000 4127</div>
    <div class="web back-web">www.tiny-sprouts.com.au</div>
    <div class="social">
      <span><i></i>Like Us @ tinysproutsOZ</span>
      <span><i></i>Follow our tweets @TinySproutsO</span>
    </div>
  </section>

</body>
</html>
```